Extremely Professional Lawyer needs letterhead for new boutique real estate law firm

I need letterhead for my new solo practice law firm. I practiced as a partner in a huge global law firm for years. Now I am starting a solo firm where I will deliver very high-quality legal services that are real-estate focused. The idea is that my practice will be very focused but that the services will be at the quality level provided by partners at high-profile law firms. The name of my law firm will be Brenn Law Group, LLC. For now, I am the only lawyer. I expect to negotiate and draft house sale/purchase contracts and close house deals. Eventually, I would like to do small-scale development deals for developer clients, a specialty of mine.

Industry/Entity Type

Boutique

```html
<!DOCTYPE html>
<html lang="en">
<head>
<meta charset="utf-8">
<title>Brenn Law Group, LLC — Letterhead</title>
<link href="https://fonts.googleapis.com/css2?family=Arimo:wght@400;600;700&display=swap" rel="stylesheet">
<style>
  :root {
    --brand-blue: #1c63b7;
    --ink: #2a2a2a;
    --muted: #555;
    --rule: #9a9a9a;
    --paper: #ffffff;
  }
  * { margin: 0; padding: 0; box-sizing: border-box; }
  html, body { width: 849px; height: 1200px; overflow: hidden; background: var(--paper); }
  body { font-family: "Arimo", Arial, sans-serif; color: var(--ink); }
  .letterhead { position: relative; width: 849px; height: 1200px; background: var(--paper); }

  .brand {
    position: absolute; top: 132px; left: 0; width: 100%;
    display: flex; justify-content: center; align-items: center; gap: 12px;
  }
  .brand-mark { width: 22px; height: 22px; background: var(--brand-blue); }
  .brand-name { font-size: 24px; font-weight: 600; color: var(--brand-blue); letter-spacing: 0.2px; }

  .letter { position: absolute; top: 306px; left: 102px; width: 620px; font-size: 13.5px; line-height: 20px; }
  .date { margin-bottom: 22px; }
  .salutation { margin-bottom: 12px; }
  .letter-body p { margin-bottom: 22px; word-break: break-all; text-align: justify; letter-spacing: 0.3px; }
  .closing { margin-top: 18px; }
  .signature { display: block; width: 150px; height: 46px; margin: 6px 0 4px; background: linear-gradient(90deg, #2d2d2d, #444); border-radius: 3px; opacity: 0.85; }

  .footer-rule { position: absolute; top: 964px; left: 102px; width: 645px; height: 1px; background: var(--rule); }
  .contacts {
    position: absolute; top: 978px; left: 102px; width: 645px;
    display: grid; grid-template-columns: 60px 14px 300px 60px 14px 1fr;
    row-gap: 6px; font-size: 13px; line-height: 16px; color: var(--muted);
  }
  .contacts .label { color: var(--brand-blue); }
  .footer-band { position: absolute; top: 1054px; left: 0; width: 100%; height: 76px; background: var(--brand-blue); }
</style>
</head>
<body>
<div class="letterhead">
  <header class="brand">
    <span class="brand-mark"></span>
    <span class="brand-name">Brenn Law Group, LLC.</span>
  </header>

  <main class="letter">
    <p class="date">May 21-05-2014</p>
    <p class="salutation">Dear Mr. Name<br>manager</p>
    <div class="letter-body">
      <p>xolxolxolxolxolxolxolxolxolxolxolxolxolxolxolxolxolxolxolxolxolxol xolxolxolx xolxolxo xolxolxolxolxol xolxolxolxol olxolxolxolxolxolxolxolxolxolxolxolxolxol xolxol xolxolxolxolxolxolxolxolxolxolxolxolxolxoxolxolxolxolxolxolxolxolxolxolxolxol xolxolxolxolxolxolxolxolxolxolxolxolxolxolxolxolxolxolxolxolxol xolxolxol xolxo xolxolxolxolxo xolxolxolxolxol olxolxolxolxolxolxolxolxolxolxolxolxolxol xolxol xolxolxolxolxolxolxolxolxolxolxolxolxolxolxolxolxolxol</p>
      <p>xolxolxolxolxolxolxolxOlxolxolxolxolxolxolxolxolxolxolxolxolxolxolxolxolxolxolxolxolxolxolxolxolxolxolxolxolxolxolxolxolxolxolxol xolxolxolxo xolxolxolxo xolxolxolxolxolxo xolxolxolxolxolxolxolxolxolxolxolxolxolxolxolxolxol</p>
      <p>xolxolxolxolxolxolxolxolxolxolxolxolxolxolxolxolxolxolxolxolxolxolxolxolxolxolxolxolxolxolxolxolxolxolxolxolxolxolxolxolxolxol xolxolxolxolxolxolxo xolxolxolxolxolxolxolxolxolxolxolxolxolxolxolxolxolxolxolxolxolxolxolxol xolxolxolxolxolxol xolxolxolxolxolxolxolxolxolxolxolxolxolxolxolxolxolxolxolxolxolxolxolxolxol</p>
    </div>
    <p class="closing">yours sincerely,</p>
    <span class="signature" role="img" aria-label="Handwritten signature of the attorney"></span>
    <p class="signer">xolxolxolxolxolxolx</p>
  </main>

  <div class="footer-rule"></div>
  <footer class="contacts">
    <span class="label">No.</span><span class="label">:</span><span>000 Xolxol, xolxo, xolxo , Country 00 000</span><span></span><span></span><span></span>
    <span class="label">e - mail</span><span class="label">:</span><span>yourid@yourmail.com</span><span class="label">Web</span><span class="label">:</span><span>yourweb.com</span>
    <span class="label">TEL</span><span class="label">:</span><span>000 000 0000</span><span class="label">FAX</span><span class="label">:</span><span>000 000 0000</span>
  </footer>
  <div class="footer-band"></div>
</div>
</body>
</html>
```